Petal Crest Arbour Rentals Spain

Why not add the WOW factor to your special occassion by bringing it to life with our beautiful selection of magnificent Blosom Tree´s.
Handmade with Silk Flowers these Tree´s look real to life adding the perfect decoration to your event or breathtaking feature for your Wedding Day.
Our Tree´s suit any theme whether its Rustic, Elegant, Fairy Tale or Enhanted.
With a versitle selection we offerf floor to ceiling and table centre pieces which can be used both inside or outdoor.
If you are looking for your Fiary Tale look no further.
Target Market(s)
Franchise , weddings and Events
Font styles to use
Requirements
Must have
- Crisp Lettering and attractive Presintation
Nice to have
- Elegant fonts and different from the rest
I am looking for a overall branding design ,including letter heads Buisness cards email signuture a4 template design ,invoising design ,Presentation folder design to hold A4 papers and usb stick ,envolope design ,flyier design ,three font designs sticker design, New logo design 3 concepts

```html
<!DOCTYPE html>
<html lang="en">
<head>
<meta charset="utf-8">
<title>Petal Crest Arbour Rentals Spain – Stationery</title>
<link href="https://fonts.googleapis.com/css2?family=Marcellus&display=swap" rel="stylesheet">
<style>
  :root {
    --backdrop: #838383;
    --paper-cream: #e8e3dd;
    --paper-white: #ffffff;
    --gold: #c9a24a;
    --gold-light: #f1df92;
    --gold-deep: #d6ad52;
    --blossom-pink: #e0579e;
    --ink: #1d1a17;
    --icon-tint: #f3ecd6;
  }
  * { margin: 0; padding: 0; box-sizing: border-box; }
  html, body {
    width: 1200px; height: 800px; overflow: hidden;
    background: var(--backdrop);
  }
  .canvas {
    position: relative; width: 1200px; height: 800px;
    font-family: "Marcellus", Georgia, serif;
  }

  /* Letterhead */
  .letterhead {
    position: absolute; left: 148px; top: 134px;
    width: 407px; height: 576px;
    background: var(--paper-cream);
  }
  .brand {
    position: absolute; display: flex; flex-direction: column; align-items: center;
    color: var(--gold); text-align: center; line-height: 1.15;
  }
  .brand-dot {
    border-radius: 50%; background: var(--blossom-pink); margin-bottom: 3px;
  }
  .letterhead .brand { left: 0; right: 0; top: 18px; font-size: 8.5px; letter-spacing: 0.4px; }
  .letterhead .brand-dot { width: 12px; height: 12px; }

  .contact-band {
    position: absolute; left: 0; bottom: 0; width: 100%; height: 18px;
    background: linear-gradient(90deg, var(--gold-deep), var(--gold-light) 50%, var(--gold-deep));
    display: flex; align-items: center; justify-content: space-between;
    padding: 0 8px; font-size: 7.6px; color: var(--ink);
  }
  .contact-item { display: flex; align-items: center; gap: 3px; white-space: nowrap; }
  .contact-icon { width: 9px; height: 9px; flex: none; }
  .social-square { width: 8px; height: 8px; background: var(--icon-tint); flex: none; }

  /* Envelope */
  .envelope {
    position: absolute; left: 658px; top: 333px;
    width: 360px; height: 180px;
    background: var(--paper-white);
  }
  .envelope .brand { left: 20px; top: 24px; width: 52px; font-size: 5.6px; letter-spacing: 0.2px; }
  .envelope .brand-dot { width: 8px; height: 8px; margin-bottom: 2px; }
</style>
</head>
<body>
<main class="canvas">

  <section class="letterhead" aria-label="Letterhead">
    <div class="brand">
      <span class="brand-dot"></span>
      <span class="brand-name">Petal Crest<br>Arbour Rentals</span>
    </div>

    <footer class="contact-band">
      <span class="contact-item">
        <svg class="contact-icon" viewBox="0 0 10 10" aria-hidden="true">
          <rect x="0.5" y="2" width="9" height="6" fill="none" stroke="var(--icon-tint)" stroke-width="1"/>
          <path d="M0.5 2 L5 5.5 L9.5 2" fill="none" stroke="var(--icon-tint)" stroke-width="1"/>
        </svg>
        info@petalcrestarbour.com
      </span>
      <span class="contact-item">
        <svg class="contact-icon" viewBox="0 0 10 10" aria-hidden="true">
          <rect x="2.5" y="0.5" width="5" height="9" rx="1" fill="none" stroke="var(--icon-tint)" stroke-width="1"/>
          <line x1="4.2" y1="8" x2="5.8" y2="8" stroke="var(--icon-tint)" stroke-width="0.8"/>
        </svg>
        612345678
      </span>
      <span class="contact-item">
        <span class="social-square" aria-hidden="true"></span>
        @petalcrestspain
      </span>
      <span class="contact-item">
        <span class="social-square" aria-hidden="true"></span>
        petalcrest_spain
      </span>
    </footer>
  </section>

  <section class="envelope" aria-label="Envelope">
    <div class="brand">
      <span class="brand-dot"></span>
      <span class="brand-name">Petal Crest<br>Arbour Rentals</span>
    </div>
  </section>

</main>
</body>
</html>
```